We need a flyer for a mail action to attract people's attention and to get new items for sale. We would like to focus on a kind of full service package, where a complete package should be advertised from a single source. Clearing out, sale guarantee, increase in value through renovation when accessing own craftsmen, home staging, etc. The flyer should be as possible to point out the benefits for the customer to have to take care of yourself. The design should be simple, elegant, yet down-to-earth and match the design and colors of the existing logo. The slogan "We Love Real Estate" should be incorporated as much as possible

please in German

We need the flyer in German please

```html
<!DOCTYPE html>
<html lang="de">
<head>
<meta charset="utf-8">
<title>AVR – Postkarte Leistungspaket</title>
<link rel="stylesheet" href="https://fonts.googleapis.com/css2?family=Libre+Baskerville:wght@400;700&family=PT+Sans+Narrow:wght@400;700&family=Montserrat:wght@600&display=swap">
<style>
  :root{
    --page:#e6e6e8;
    --brand-blue:#0a0fc8;
    --brand-deep:#06087a;
    --logo-navy:#0c0c86;
    --footer:#2b2a2a;
    --white:#ffffff;
    --ink:#1d1d1f;
    --silver:#d4d4d8;
    --line:#c9c9cc;
  }
  *{margin:0;padding:0;box-sizing:border-box}
  html,body{width:879px;height:1200px;overflow:hidden}
  body{background:var(--page);position:relative;font-family:"Libre Baskerville",Georgia,serif}
  .card{position:absolute;left:54px;width:793px;height:519px;overflow:hidden;background:var(--white);box-shadow:0 4px 14px rgba(0,0,0,.25)}
  .card--front{top:75px}
  .card--back{top:628px}
  .card__art{position:absolute;inset:0;width:793px;height:519px}
  .abs{position:absolute}

  /* front */
  .front__claim{right:486px;text-align:right;color:var(--white);font-family:"PT Sans Narrow",Arial,sans-serif;text-shadow:0 1px 3px rgba(0,0,0,.5)}
  .front__claim-small{top:211px;font-size:17px;white-space:nowrap}
  .front__claim-big{top:235px;font-size:28px;white-space:nowrap}
  .brand-name{color:var(--logo-navy);font-family:"Libre Baskerville",Georgia,serif;font-weight:700;letter-spacing:4px;line-height:1}
  .front__brand{top:42px;left:538px;width:208px;text-align:center;font-size:56px}
  .front__slogan{top:104px;left:506px;width:272px;text-align:center;color:var(--logo-navy);font-weight:700;font-size:20px;letter-spacing:2.5px;white-space:nowrap}

  .contact-lead{color:var(--white);font-size:17px;letter-spacing:.5px;text-align:center;white-space:nowrap}
  .phone-pill{display:flex;align-items:center;justify-content:center;gap:12px;height:31px;border-radius:16px;background:linear-gradient(#ffffff,#d9d9dc);font-family:"Montserrat",Arial,sans-serif;font-weight:600;font-size:22px;color:var(--ink)}
  .phone-pill svg{width:22px;height:22px}
  .front__lead{top:402px;left:0;width:814px}
  .front__phone{top:429px;left:214px;width:371px}
  .site-footer{position:absolute;left:0;bottom:0;width:793px;height:34px;background:var(--footer);color:var(--white);font-size:15px;letter-spacing:2.5px;display:flex;align-items:center;justify-content:center}
  .front__footer{padding-right:0}

  /* back */
  .back__title{top:36px;left:22px;color:var(--white);font-size:29px;font-weight:700;letter-spacing:.5px}
  .back__intro{top:75px;left:22px;color:var(--white);font-size:14px;line-height:15px;font-weight:700}
  .back__package{top:170px;left:22px;color:var(--ink);font-size:21px;letter-spacing:.5px}
  .services{top:229px;left:29px;list-style:none;font-size:14px;line-height:17px;color:var(--ink)}
  .services li{position:relative;padding-left:20px}
  .services li::before{content:"";position:absolute;left:0;top:4px;width:9px;height:9px;background:var(--brand-blue);clip-path:polygon(0 0,100% 50%,0 100%,30% 50%)}
  .back__brand{top:28px;left:411px;font-size:40px;letter-spacing:3px}
  .stamp-box{top:18px;left:637px;width:138px;height:93px;border:1px solid #9a9a9e}
  .address-line{left:479px;width:295px;height:1px;background:var(--line)}
  .back__lead{top:400px;left:0;width:415px}
  .back__phone{top:427px;left:56px;width:304px}
  .back__footer{justify-content:center;padding-right:12px}
</style>
</head>
<body>

<section class="card card--front">
  <svg class="card__art" viewBox="0 0 793 519" aria-hidden="true">
    <defs>
      <linearGradient id="cityTone" x1="0" y1="0" x2="1" y2="1">
        <stop offset="0" stop-color="#3f67b6"/><stop offset=".45" stop-color="#c9b94a"/><stop offset="1" stop-color="#8fa57a"/>
      </linearGradient>
      <radialGradient id="suitTone" cx=".55" cy=".5" r=".7">
        <stop offset="0" stop-color="#4a7f97"/><stop offset=".6" stop-color="#243a4e"/><stop offset="1" stop-color="#16202c"/>
      </radialGradient>
      <linearGradient id="bandBlue" x1="0" y1="0" x2="0" y2="1">
        <stop offset="0" stop-color="#0a10d6"/><stop offset="1" stop-color="#05077e"/>
      </linearGradient>
      <linearGradient id="silverSweep" x1="0" y1="0" x2="1" y2="0">
        <stop offset="0" stop-color="#9c9ca2"/><stop offset=".7" stop-color="#f2f2f4"/><stop offset="1" stop-color="#b5b5ba"/>
      </linearGradient>
    </defs>
    <rect width="793" height="519" fill="url(#cityTone)" role="img" aria-label="Abendliche Stadtansicht von oben"/>
    <path d="M0 0 H296 C340 70 362 160 358 235 C354 300 342 345 324 420 L0 430 Z" fill="url(#suitTone)" role="img" aria-label="Geschäftsmann im Anzug mit geöffneten Händen und leuchtendem Haussymbol"/>
    <path d="M296 0 C340 70 362 160 358 235 C354 300 342 345 324 420" fill="none" stroke="url(#silverSweep)" stroke-width="7"/>
    <path d="M0 424 C180 395 500 360 793 372 V420 C620 395 420 385 0 424 Z" fill="url(#silverSweep)"/>
    <path d="M0 424 C200 395 430 380 560 384 C670 388 740 400 793 418 V519 H0 Z" fill="url(#bandBlue)"/>
    <path d="M560 382 C670 386 740 398 793 414" fill="none" stroke="#111" stroke-width="3"/>
  </svg>

  <p class="abs front__claim front__claim-small">Ein komplettes Paket sollte aus einer Hand</p>
  <p class="abs front__claim front__claim-big">beworben werden</p>

  <div class="abs brand-name front__brand">AVR</div>
  <p class="abs front__slogan">We Love Real Estate</p>

  <p class="abs contact-lead front__lead">Nehmen Sie Kontakt mit uns auf</p>
  <div class="abs phone-pill front__phone">
    <svg viewBox="0 0 24 24" aria-hidden="true"><circle cx="12" cy="12" r="10.5" fill="none" stroke="#1d1d1f" stroke-width="1.6"/><path d="M8.3 6.6l1.8-.4 1.3 2.8-1.2.9c.6 1.5 1.6 2.6 3 3.3l1-1.1 2.7 1.4-.4 1.8c-3.9.3-8.3-4.1-8.2-8.7z" fill="#1d1d1f"/></svg>
    <span>123-456-5678</span>
  </div>
  <div class="site-footer front__footer">www.Webseite.com</div>
</section>

<section class="card card--back">
  <svg class="card__art" viewBox="0 0 793 519" aria-hidden="true">
    <defs>
      <radialGradient id="backBlue" cx=".75" cy=".45" r=".9">
        <stop offset="0" stop-color="#0c12e0"/><stop offset=".7" stop-color="#0a0fb8"/><stop offset="1" stop-color="#07098a"/>
      </radialGradient>
      <linearGradient id="panelGrey" x1="0" y1="0" x2="0" y2="1">
        <stop offset="0" stop-color="#ffffff"/><stop offset="1" stop-color="#d6d6d8"/>
      </linearGradient>
      <linearGradient id="panelShadow" x1="0" y1="0" x2="0" y2="1">
        <stop offset="0" stop-color="#000" stop-opacity=".55"/><stop offset="1" stop-color="#000" stop-opacity="0"/>
      </linearGradient>
    </defs>
    <path d="M0 0 H339 C404 70 442 150 442 230 C442 320 424 420 386 485 H0 Z" fill="var(--silver)"/>
    <path d="M0 0 H335 C400 70 437 150 437 230 C437 320 419 420 380 485 H0 Z" fill="url(#backBlue)"/>
    <path d="M0 158 H241 C250 158 254 162 258 170 L265 187 H0 Z" fill="#ffffff"/>
    <rect x="0" y="187" width="465" height="168" fill="url(#panelGrey)"/>
    <path d="M0 355 H465 L430 362 H0 Z" fill="#111"/>
    <rect x="0" y="358" width="430" height="40" fill="url(#panelShadow)"/>
  </svg>

  <h1 class="abs back__title">WIR MÖCHTEN</h1>
  <p class="abs back__intro">Ein komplettes Paket sollte aus einer Hand<br>beworben werden</p>

  <h2 class="abs back__package" style="font-weight:400">LEISTUNGSPAKET</h2>
  <ul class="abs services">
    <li>Aufräumen</li>
    <li>Verkaufsgarantie</li>
    <li>Wertsteigerung durch Renovierung beim Zugang<br>eigene Handwerker</li>
    <li>Home Inszenierung</li>
    <li>Etc</li>
  </ul>

  <div class="abs brand-name back__brand">AVR</div>
  <div class="abs stamp-box"></div>
  <div class="abs address-line" style="top:215px"></div>
  <div class="abs address-line" style="top:249px"></div>
  <div class="abs address-line" style="top:283px"></div>
  <div class="abs address-line" style="top:317px"></div>

  <p class="abs contact-lead back__lead">Nehmen Sie Kontakt mit uns auf</p>
  <div class="abs phone-pill back__phone">
    <svg viewBox="0 0 24 24" aria-hidden="true"><circle cx="12" cy="12" r="10.5" fill="none" stroke="#1d1d1f" stroke-width="1.6"/><path d="M8.3 6.6l1.8-.4 1.3 2.8-1.2.9c.6 1.5 1.6 2.6 3 3.3l1-1.1 2.7 1.4-.4 1.8c-3.9.3-8.3-4.1-8.2-8.7z" fill="#1d1d1f"/></svg>
    <span>123-456-5678</span>
  </div>
  <div class="site-footer back__footer">www.Webseite.com</div>
</section>

</body>
</html>
```